The Fern Barrel Pub- restaurant menu, new launch

This is a new restaurant launching Summer 2017. Restaurant is a conversion of long standing small town existing family pizza/italian restaurant. new concept shifts concept to a family pub atmosphere featuring familiar appetizers, burgers, wood-fired pizza, and daily specials, draft beer, full- bar.

atmosphere is casual. want menu to reflect a more current "vibe" than the old place did. Not cold and modern, but retain the cozy familiar feel, without seeming dated and old fashioned.

4 panel menu; 8.5 X 11; 2-4 color
Updates

Project Deadline Extended
Reason: I am interested in seeing more designs. I will be providing feedback in the next few days on all designs submitted. I will also be increasing the budget.

Target Market(s)

Family-Oriented Pub, rural location Berkshire County, MA. Mostly Blue collar customer, value oriented

Industry/Entity Type

American Restaurant

Font styles to use
Sans Serif

Colors

Designer to choose colors to be used in the design.

Requirements
Must have
• Clear, uncluttered design, Highlighted items as specified in draft file (to come)
• ability to make changes daily as menu changes
• each panel separate sheet to slide into binder sleeve

```html
<!DOCTYPE html>
<html lang="en">
<head>
<meta charset="utf-8">
<title>The Fern Barrel Pub – Menu Sheets</title>
<link href="https://fonts.googleapis.com/css2?family=Anton&family=Oswald:wght@300;400&family=Sancreek&family=Old+Standard+TT:wght@700&family=Fira+Sans+Condensed:wght@400;600&display=swap" rel="stylesheet">
<style>
:root{
  --backdrop:#2c3d4e;
  --paper-light:#efdcab;
  --paper-mid:#dfc48a;
  --paper-dark:#c6a464;
  --ink:#3a281c;
  --ink-soft:#4a3526;
  --box:#44291a;
  --box-text:#f2e4c4;
  --rule:#5a4331;
}
*{margin:0;padding:0;box-sizing:border-box}
html,body{width:1200px;height:1200px;overflow:hidden;background:var(--backdrop)}
.canvas{position:relative;width:1200px;height:1200px;overflow:hidden}
.sheet{
  position:absolute;width:558px;height:722px;color:var(--ink);
  background:radial-gradient(ellipse at 40% 35%,var(--paper-light) 0%,var(--paper-mid) 55%,var(--paper-dark) 100%);
  box-shadow:0 4px 14px rgba(0,0,0,.45);
}
.sheet > *{position:absolute;white-space:nowrap}
.sheet--starters{left:20px;top:40px}
.sheet--pizza{left:604px;top:40px;width:556px}
.sheet--burgers{left:78px;top:512px;height:720px}
.sheet--specials{left:668px;top:478px;width:540px;height:740px}

.heavy{font-family:"Anton",sans-serif;font-weight:400}
.cond{font-family:"Oswald",sans-serif;font-weight:400}
.swash{font-family:"Sancreek",serif}
.serif{font-family:"Old Standard TT",serif;font-weight:700}
.body{font-family:"Fira Sans Condensed",sans-serif;font-size:10px;line-height:1.32;white-space:normal}
.caps{text-transform:uppercase}
.rule{height:2px;background:var(--rule);left:34px;right:32px}
.price{font-family:"Oswald",sans-serif;font-weight:400}

/* starters */
.dash-rule{left:34px;top:110px;width:490px;height:6px;
  background:repeating-linear-gradient(90deg,var(--ink) 0 62px,transparent 62px 72px)}

/* burgers feature box */
.feature-box{left:27px;top:190px;width:491px;height:102px;background:var(--box);border-radius:10px;color:var(--box-text)}
.feature-box > *{position:absolute;white-space:nowrap}
.feature-box > .feature-desc{white-space:normal;left:38px;top:58px;width:430px}
</style>
</head>
<body>
<div class="canvas">

  <!-- Starters sheet -->
  <section class="sheet sheet--starters">
    <h1 class="heavy" style="left:34px;top:34px;font-size:60px;line-height:1">LET'S GET <span class="swash" style="font-size:66px">S</span><span class="cond" style="font-size:64px">TARTED</span></h1>
    <div class="dash-rule"></div>

    <div style="left:34px;top:128px;line-height:1"><span class="cond" style="font-size:44px;font-weight:300">WINGS</span><span class="price" style="font-size:30px"> $12</span></div>
    <p class="body" style="left:222px;top:132px;width:310px">A Baker's Ten (that's 11) of the biggest tastiest wings you'll find anywhere. Choose from our award-winning sauces: <span class="caps">Buffalo Mild, Buffalo Hot, Maple's Honey Chipotle, Garlic Parm, BBQ, Xtra Hot, Challenge Hot*</span></p>
    <div class="rule" style="top:196px"></div>

    <div class="cond" style="left:34px;top:206px;font-size:42px;font-weight:300;line-height:1">BONELESS</div>
    <div style="left:34px;top:248px;line-height:1"><span class="serif" style="font-size:44px">wings</span><span class="price" style="font-size:30px"> $12</span></div>
    <p class="serif" style="left:222px;top:214px;font-size:19px">Why are they called wings?</p>
    <p class="body" style="left:222px;top:240px;width:300px">They're not wings.<br>But it's tasty boneless breaded chicken anyway.<br>Same great sauces, 8 "Wings."</p>
    <div class="rule" style="top:306px"></div>

    <div style="left:30px;top:318px;line-height:1"><span class="heavy" style="font-size:64px">'CHOS!!</span><span class="price" style="font-size:30px"> $11</span></div>
    <p class="serif" style="left:271px;top:326px;font-size:18px;line-height:.92">Totchos and Nachos<br>and Cheese, oh my!</p>
    <p class="body caps" style="left:271px;top:368px;width:255px">Add brisket $3 | Add pulled pork $3 | Add chili $3</p>
    <div class="rule" style="top:412px"></div>

    <div class="cond" style="left:34px;top:424px;font-size:36px;line-height:1">SPINACH <span class="swash">A</span>RTICHOKE <span class="swash">D</span>IP<span class="price" style="font-size:28px">$10</span></div>
  </section>

  <!-- Pizza sheet -->
  <section class="sheet sheet--pizza">
    <h1 class="heavy" style="left:31px;top:40px;font-size:60px;line-height:1">WOOD FIRED <span class="swash" style="font-size:64px">P</span><span class="heavy">IZZA</span></h1>
    <p class="body" style="left:31px;top:118px;width:500px">All our dough is made fresh daily in house with just four ingredients- water flour salt and yeast. Baked to perfection in the wood oven, Fern Barrel Pizza is the best in the county!</p>
    <div class="rule" style="top:158px;left:31px"></div>

    <div class="cond" style="left:31px;top:172px;font-size:32px;line-height:1"><span class="swash">O</span>UR <span class="swash">S</span>PECIALTY <span class="swash">P</span>IES- SM$13 LG$17</div>

    <div style="left:31px;top:228px;line-height:1"><span class="heavy" style="font-size:40px">THE BUFFALO</span><span class="serif" style="font-size:46px"> Bird</span></div>
    <p class="body" style="left:354px;top:232px;width:160px">Buffalo sauce, grilled chicken, mozzarella and topped with red onion for just the right finish. Don't like onion? We'll leave it off!</p>

    <div style="left:31px;top:298px;line-height:1"><span class="heavy" style="font-size:40px">CHICKEN</span><span class="serif" style="font-size:50px"> 'Q</span></div>
    <p class="body" style="left:241px;top:304px;width:270px">House made BBQ sauce from Oak Pit BBQ, Grilled chicken and mozzarella make this crowd favorite.</p>

    <div style="left:31px;top:360px;line-height:1"><span class="serif" style="font-size:50px">The</span><span class="swash" style="font-size:40px"> H</span><span class="cond" style="font-size:40px">ULA</span><span class="serif" style="font-size:50px">Hula</span></div>
    <p class="body" style="left:354px;top:362px;width:160px">Sliced ham and Pineapple, and mozzarella. It doesn't get any better!<br><span class="caps">Ask for coconut, if you're feeling crazy!</span></p>
    <p class="body caps" style="left:31px;top:420px;width:300px">Gluten free, available in small size only- add $2.00</p>
  </section>

  <!-- Burgers sheet -->
  <section class="sheet sheet--burgers">
    <h1 style="left:33px;top:40px;line-height:1"><span class="swash" style="font-size:66px">F</span><span class="heavy" style="font-size:58px">ERN BURGERS</span></h1>
    <p class="body" style="left:33px;top:120px;width:490px">Our ground beef is pure 80/20 goodness, from Northeast farms, Always fresh, hand packed daily for exceptional beef burger taste. <span class="serif" style="font-size:13px">Accept no substitutes- these are the best burgers anywhere.</span></p>

    <div class="feature-box">
      <div style="left:10px;top:10px;line-height:1"><span class="swash" style="font-size:32px">T</span><span class="cond" style="font-size:30px">HE </span><span class="heavy" style="font-size:30px">FERN BURGER</span><span class="serif" style="font-size:32px"> "Original"</span><span class="price" style="font-size:30px">$10.99</span></div>
      <p class="body feature-desc">Double ¼ lb hand packed patties, with double American cheese, and double the Green Hills Smokehouse Applewood Bacon. This beauty is served with Lettuce, Tomato, Onion, our world-class hand-cut fries, and a side of Fern Sauce.</p>
    </div>

    <p class="serif" style="left:33px;top:304px;font-size:29px">Want to do it your way?</p>
    <div style="left:378px;top:306px;line-height:.95"><span class="cond" style="font-size:28px;font-weight:300"><span class="swash">O</span>VER 100</span><br><span class="serif" style="font-size:28px">possibilities!</span></div>

    <p class="body caps" style="left:33px;top:342px;width:170px;font-weight:600;font-size:10px"><span style="font-size:14px">¼ LB Patty</span> $6.00<br>Double ¼ $8.00<br>Triple ¼ $9.00<br>Quad quarter $10.00</p>
    <p class="body caps" style="left:210px;top:342px;width:170px;font-weight:600;font-size:10px"><span style="font-size:14px">1/3 LB Patty</span> $8.00<br>Double 1/3 $11.00<br>Triple 1/3 $13.00<br>Quad 1/3 $15.00</p>

    <p class="serif" style="left:33px;top:412px;font-size:15px">add-ons</p>
    <p class="body caps" style="left:33px;top:430px;width:420px;font-weight:600">Lettuce, tomato, onion, pickle- no charge<br>Sliced cheese- American, cheddar, Swiss .75 per<br>Gorgonzola $1.00</p>
    <div class="rule" style="top:484px;left:33px;right:28px"></div>

    <div class="cond" style="left:33px;top:498px;font-size:25px;line-height:1"><span class="swash">G</span>REEN HILLS <span class="swash">S</span>MOKEHOUSE</div>
    <div style="left:33px;top:526px;line-height:1"><span class="serif" style="font-size:28px">Applewood Bacon</span><span class="price" style="font-size:28px">$1.00<span style="font-size:20px">PER</span></span></div>
    <div class="rule" style="top:586px;left:33px;right:28px"></div>

    <div class="cond" style="left:33px;top:604px;font-size:27px;line-height:1"><span class="swash">W</span>ORLD-<span class="swash">C</span>LASS</div>
    <div style="left:33px;top:636px;line-height:1"><span class="serif" style="font-size:28px">Hand-cut Fries</span><span class="price" style="font-size:32px"> $2.50</span></div>
  </section>

  <!-- Daily specials sheet -->
  <section class="sheet sheet--specials">
    <h1 style="left:64px;top:38px;line-height:1"><span class="swash" style="font-size:66px">D</span><span class="cond" style="font-size:58px">AILY</span><span class="swash" style="font-size:66px">S</span><span class="cond" style="font-size:58px">PECIALS-</span></h1>
    <p class="serif" style="left:92px;top:122px;font-size:28px">where the craziness happens</p>

    <div style="left:34px;top:172px;line-height:1"><span class="serif" style="font-size:38px">20</span><span class="swash" style="font-size:36px"> L</span><span class="cond" style="font-size:36px">AYER </span><span class="heavy" style="font-size:36px">LASAGNA</span><span class="price" style="font-size:34px">&nbsp; $12.99</span></div>
    <p class="body" style="left:34px;top:226px;width:480px">Our signature dish. Sells out every week, get it when you can</p>
    <div class="rule" style="top:252px"></div>

    <div style="left:34px;top:258px;line-height:1"><span class="serif" style="font-size:50px">The </span><span class="heavy" style="font-size:40px">PIG </span><span class="swash" style="font-size:40px">P</span><span class="cond" style="font-size:40px">ILE</span><span class="price" style="font-size:34px">&nbsp; $11</span></div>
    <p class="body" style="left:34px;top:312px;width:480px">Our World-class Hand-cut fries topped with Pulled pork, Mozzarella, Crispy Bacon, BBQ sauce, and Topped with house onion rings. Not for the faint of heart, if you know what we mean...</p>
    <div class="rule" style="top:352px"></div>

    <div style="left:34px;top:362px;line-height:1"><span class="heavy" style="font-size:38px">PASTA </span><span class="swash" style="font-size:38px">P</span><span class="cond" style="font-size:36px">RIMAVERA</span><span class="price" style="font-size:34px">&nbsp; $12.99</span></div>
    <p class="body" style="left:34px;top:410px;width:480px">Fresh veggies, tossed with penne, in a garlic white wine butter sauce</p>
    <div class="rule" style="top:436px"></div>

    <div style="left:34px;top:446px;line-height:1"><span class="swash" style="font-size:38px">C</span><span class="cond" style="font-size:36px">HICKEN </span><span class="heavy" style="font-size:38px">PARMESAN</span><span class="price" style="font-size:34px">&nbsp; $15</span></div>
    <p class="body" style="left:34px;top:496px;width:480px">Two breaded chicken breasts topped with house marinara and mozzarella, served with penne marinara. Yum.</p>
    <div class="rule" style="top:532px"></div>

    <div style="left:34px;top:544px;line-height:1"><span class="heavy" style="font-size:38px">PASTA </span><span class="swash" style="font-size:38px">C</span><span class="cond" style="font-size:36px">ARBONARA</span><span class="price" style="font-size:34px">&nbsp; $15</span></div>
    <p class="body" style="left:34px;top:594px;width:480px">The creamy bacon pasta classic. You know it, you love it. Just say yes.</p>
    <div class="rule" style="top:618px"></div>

    <div style="left:34px;top:628px;line-height:1"><span class="serif" style="font-size:38px">Buffalo</span><span class="swash" style="font-size:34px"> C</span><span class="cond" style="font-size:32px">HICKEN</span><span class="heavy" style="font-size:34px">MAC&amp;CHEESE</span><span class="price" style="font-size:32px">&nbsp; $13</span></div>
    <p class="body" style="left:34px;top:680px;width:480px">All the food groups in this one! Chicken, Buffalo sauce, Mac and Cheese. A true food pyramid!</p>
  </section>

</div>
</body>
</html>
```